Etikette für eine Flasche 0.375L
Zielgruppe
Die Flasche soll anziehend sein obwohl der Inhalt noch nicht probiert wurde.
Zielgruppe, jedermann-jederfrau... Der Gesamteindruck soll der Flasche zum verkauf verhelfen.
Aufgabenstellung
Suche ein Logo für eine Glasflasche. Inhalt 0.375Liter (nomale Glasflaschenform)
Das Logo soll sehr kreastive, klar, auffallend (aber nicht in der Farbe).
Es kann rund, Oval, Eckig, 3-12 Eckig sein, egal...
Farblich kann es in Schwarz oder in einem dünkleren Kontrast sein. Der Eierlikör ist Beige-hellbeige wie eine Vanillesauce. Es kann mehrfarbig sein. Darf auch Gold oder Silber enthalten.
Das Logo soll exklusive wirken, einen Wow-effekt. Ein Getränk in der Flasche die jeden anzieht und jeder möchte es kaufen.
Mein Logo "feinbrauwerk.ch" muss auf der Flasche vorhanden sein

```html
<!DOCTYPE html>
<html lang="de">
<head>
<meta charset="utf-8">
<title>NOBLE'NOG – Flaschenetikette</title>
<link rel="stylesheet" href="https://fonts.googleapis.com/css2?family=Montserrat:wght@500;700&display=swap">
<style>
  :root {
    --canvas: #ffffff;
    --label-ink: #221f1f;
    --label-cream: #c6c3ae;
    --label-cream-soft: rgba(198, 195, 174, 0.55);
  }
  html, body {
    margin: 0;
    padding: 0;
    width: 1200px;
    height: 1200px;
    overflow: hidden;
    background: var(--canvas);
  }
  .canvas {
    width: 1200px;
    height: 1200px;
    display: flex;
    align-items: center;
    justify-content: center;
  }
  .label-shield {
    width: 740px;
    height: 981px;
    display: block;
  }
  .shield-rim { fill: var(--label-cream); }
  .shield-body { fill: var(--label-ink); }
  .emblem-ring {
    fill: none;
    stroke: var(--label-cream-soft);
    stroke-width: 0.8;
  }
  .star { fill: var(--label-cream); }
  .wordmark {
    font-family: "Montserrat", sans-serif;
    font-weight: 700;
    font-size: 36px;
    letter-spacing: -0.5px;
    fill: var(--label-cream);
  }
  .usage-note {
    font-family: "Montserrat", sans-serif;
    font-weight: 500;
    font-size: 8.5px;
    letter-spacing: 1px;
    fill: var(--label-cream);
  }
  .rooster-area { fill: url(#roosterTone); }
</style>
</head>
<body>
<main class="canvas">
  <svg class="label-shield" viewBox="0 0 400 530" xmlns="http://www.w3.org/2000/svg" aria-label="Etikette NOBLE'NOG Eierlikör">
    <defs>
      <radialGradient id="roosterTone" cx="50%" cy="50%" r="60%">
        <stop offset="0%" stop-color="#c6c3ae" stop-opacity="0.85"/>
        <stop offset="100%" stop-color="#c6c3ae" stop-opacity="0.45"/>
      </radialGradient>
    </defs>

    <path class="shield-rim" d="M0,0 Q200,24 400,0 C392,90 392,160 396,260 C400,360 330,440 200,530 C70,440 0,360 4,260 C8,160 8,90 0,0 Z"/>
    <path class="shield-body" d="M11,11 Q200,33 389,11 C382,95 382,162 386,260 C389,354 322,430 200,517 C78,430 11,354 14,260 C18,162 18,95 11,11 Z"/>

    <text class="wordmark" x="200" y="80" text-anchor="middle">NOBLE'NOG</text>

    <circle class="emblem-ring" cx="200" cy="273" r="165"/>

    <rect class="rooster-area" x="88" y="182" width="240" height="224" rx="24" role="img" aria-label="Illustration eines stolzen Hahns mit kleiner Krone"/>

    <g class="stars">
      <polygon class="star" points="30,317 31.8,321.5 36.5,321.5 32.7,324.3 34.1,328.8 30,326 25.9,328.8 27.3,324.3 23.5,321.5 28.2,321.5"/>
      <polygon class="star" points="47,362 48.9,366.8 54,366.8 49.9,369.8 51.4,374.6 47,371.6 42.6,374.6 44.1,369.8 40,366.8 45.1,366.8"/>
      <polygon class="star" points="72,396 74.2,401.4 80,401.4 75.3,404.8 77,410.2 72,406.8 67,410.2 68.7,404.8 64,401.4 69.8,401.4"/>
      <polygon class="star" points="106,420 108.3,425.6 114.4,425.6 109.5,429.2 111.3,434.9 106,431.3 100.7,434.9 102.5,429.2 97.6,425.6 103.7,425.6"/>
      <polygon class="star" points="370,317 371.8,321.5 376.5,321.5 372.7,324.3 374.1,328.8 370,326 365.9,328.8 367.3,324.3 363.5,321.5 368.2,321.5"/>
      <polygon class="star" points="353,362 354.9,366.8 360,366.8 355.9,369.8 357.4,374.6 353,371.6 348.6,374.6 350.1,369.8 346,366.8 351.1,366.8"/>
      <polygon class="star" points="328,396 330.2,401.4 336,401.4 331.3,404.8 333,410.2 328,406.8 323,410.2 324.7,404.8 320,401.4 325.8,401.4"/>
      <polygon class="star" points="294,420 296.3,425.6 302.4,425.6 297.5,429.2 299.3,434.9 294,431.3 288.7,434.9 290.5,429.2 285.6,425.6 291.7,425.6"/>
      <polygon class="star" points="200,489 202.6,495.4 209.5,495.4 203.9,499.5 206,506 200,502 194,506 196.1,499.5 190.5,495.4 197.4,495.4"/>
    </g>

    <text class="usage-note" x="200" y="455" text-anchor="middle">VOR GEBRAUCH GUT</text>
    <text class="usage-note" x="200" y="470" text-anchor="middle">SCHÜTTELN</text>
  </svg>
</main>
</body>
</html>
```